Business Card/Letterhead/Envelope design
KTL & Associates
Business Card/Letterhead/Envelope design -
Creative Brief
Professional
Gregory P. Holt
Principal
2947 Brambleton Way Suite 340 Frisco, Texas 75981
gregory@ktlva.com
www.ktlva.com
Rounded corners preferable Simple Clean Cutting Edge Front: Full Color on White background or Full Color on Black background Back: Full Color on Black background
Reversed Logo centered on the back of card w/slogan of company... Passion. Performance. Results. (Black background)

```html
<!DOCTYPE html>
<html lang="en">
<head>
<meta charset="utf-8">
<title>KTL &amp; Associates — Stationery Set</title>
<link href="https://fonts.googleapis.com/css2?family=Roboto:wght@400;700&display=swap" rel="stylesheet">
<style>
  :root{
    --stage:#3b3b3d;
    --red:#c8161d;
    --red-dark:#8e0d12;
    --ink:#222;
    --paper:#ffffff;
    --card-black:#141414;
    --faint:#ededed;
    --soft:#dddddd;
  }
  *{box-sizing:border-box;margin:0;padding:0}
  html,body{width:1200px;height:310px;overflow:hidden}
  body{background:var(--stage);font-family:"Roboto",Arial,sans-serif;position:relative;color:var(--ink)}
  .piece{position:absolute;background:var(--paper);overflow:hidden;box-shadow:0 2px 5px rgba(0,0,0,.45)}
  .swoosh{position:absolute;left:0;bottom:0;width:100%;display:block}
  .wordmark{font-family:"Roboto",Arial,sans-serif;font-weight:700;color:var(--red);white-space:nowrap;line-height:1}
  .tiny{font-size:5px;line-height:1.4;color:var(--ink);white-space:nowrap}
  .watermark{position:absolute;left:0;width:100%;text-align:center;font-weight:700;color:var(--faint);line-height:1}

  /* brand block */
  .brand-block{position:absolute;left:8px;top:10px;width:200px}
  .brand-block .wordmark{font-size:20px}
  .brand-block .tagline{color:var(--soft);font-size:9px;margin-top:6px}
  .brand-block .slogan{color:var(--red);font-size:7px;margin-top:4px}

  /* business cards */
  .card{width:126px;height:84px;border-radius:4px}
  .card .wordmark{position:absolute;left:8px;top:8px;font-size:9px}
  .card .contact{position:absolute;left:8px;top:22px}
  .card-front-a{left:6px;top:126px}
  .card-front-b{left:142px;top:126px}
  .card-back{left:6px;top:220px;height:64px;background:var(--card-black)}
  .card-back .wordmark{left:50%;top:20px;transform:translateX(-50%);font-size:10px}
  .card-back .slogan{position:absolute;width:100%;top:36px;text-align:center;color:#ccc;font-size:5px}
  .card-plain{left:142px;top:220px;height:64px}
  .card-plain .wordmark{left:50%;top:27px;transform:translateX(-50%);font-size:10px}

  /* letterheads */
  .letterhead{width:141px;height:250px;top:19px}
  .letterhead-a{left:281px}
  .letterhead-b{left:434px}
  .letterhead .wordmark{position:absolute;left:10px;top:12px;font-size:8px}
  .letterhead .sender{position:absolute;right:10px;top:24px;text-align:right;font-size:4.5px}
  .letterhead .watermark{top:80px;font-size:46px}
  .letterhead .footer{position:absolute;left:0;bottom:5px;width:100%;text-align:center;color:#fff;font-size:4.5px}

  /* #10 envelopes */
  .envelope{width:231px;height:96px;left:700px}
  .envelope-a{top:53px}
  .envelope-b{top:178px}
  .envelope .wordmark{position:absolute;left:10px;top:10px;font-size:9px}
  .envelope .sender{position:absolute;left:10px;top:23px}
  .envelope .watermark{top:24px;font-size:38px}

  /* DL envelopes */
  .dl{width:250px;height:108px;left:943px}
  .dl-back{top:48px}
  .dl-front{top:178px;height:104px}
  .dl .wordmark{position:absolute;left:50%;transform:translateX(-50%);font-size:11px}
  .dl-back .wordmark{top:16px;color:#fff}
  .dl-front .wordmark{top:56px}
  .flap{position:absolute;left:0;top:0;width:100%;height:100%}
</style>
</head>
<body>

<section class="brand-block">
  <div class="wordmark">KTL &amp; Associates</div>
  <p class="tagline">Business Sales Mergers &amp; Acquisitions</p>
  <p class="slogan">Passion. Performance. Results.</p>
</section>

<!-- business card fronts -->
<article class="piece card card-front-a">
  <div class="wordmark">KTL &amp; Associates</div>
  <div class="contact tiny">
    <strong>Gregory P. Holt</strong><br>Principal<br>
    2947 Brambleton Way Suite 340<br>Frisco, Texas 75981<br>
    (972) 555-0148 · gregory@ktlva.com<br>www.ktlva.com
  </div>
  <svg class="swoosh" viewBox="0 0 126 14" height="14" preserveAspectRatio="none">
    <path d="M0 14 Q60 0 126 4 L126 14 Z" fill="var(--red)"/>
    <path d="M0 14 Q60 4 126 9 L126 14 Z" fill="var(--red-dark)"/>
  </svg>
</article>

<article class="piece card card-front-b">
  <div class="wordmark">KTL &amp; Associates</div>
  <div class="contact tiny">
    <strong>Gregory P. Holt</strong><br>Principal<br>
    2947 Brambleton Way Suite 340<br>Frisco, Texas 75981<br>
    (972) 555-0148 · gregory@ktlva.com<br>www.ktlva.com
  </div>
  <svg class="swoosh" viewBox="0 0 126 14" height="14" preserveAspectRatio="none">
    <path d="M0 4 Q60 16 126 2 L126 14 L0 14 Z" fill="var(--red)"/>
  </svg>
</article>

<!-- business card backs -->
<article class="piece card card-back">
  <div class="wordmark">KTL &amp; Associates</div>
  <p class="slogan">Passion. Performance. Results.</p>
</article>

<article class="piece card card-plain">
  <div class="wordmark">KTL &amp; Associates</div>
</article>

<!-- letterheads -->
<article class="piece letterhead letterhead-a">
  <div class="wordmark">KTL &amp; Associates</div>
  <div class="sender tiny">2947 Brambleton Way Suite 340<br>Frisco, Texas 75981<br>www.ktlva.com</div>
  <div class="watermark">KTL</div>
  <svg class="swoosh" viewBox="0 0 141 30" height="30" preserveAspectRatio="none">
    <path d="M0 6 Q70 26 141 2 L141 30 L0 30 Z" fill="var(--red)"/>
    <path d="M0 15 Q70 32 141 11 L141 30 L0 30 Z" fill="var(--red-dark)"/>
  </svg>
  <p class="footer">(972) 555-0148 · gregory@ktlva.com</p>
</article>

<article class="piece letterhead letterhead-b">
  <div class="wordmark">KTL &amp; Associates</div>
  <div class="sender tiny">2947 Brambleton Way Suite 340<br>Frisco, Texas 75981<br>www.ktlva.com</div>
  <div class="watermark">KTL</div>
  <svg class="swoosh" viewBox="0 0 141 30" height="30" preserveAspectRatio="none">
    <path d="M0 30 Q60 0 141 8 L141 30 Z" fill="var(--red)"/>
    <path d="M0 30 Q60 9 141 17 L141 30 Z" fill="var(--red-dark)"/>
  </svg>
  <p class="footer">Passion. Performance. Results.</p>
</article>

<!-- #10 envelopes -->
<article class="piece envelope envelope-a">
  <div class="watermark">KTL</div>
  <div class="wordmark">KTL &amp; Associates</div>
  <div class="sender tiny">2947 Brambleton Way Suite 340<br>Frisco, Texas 75981</div>
  <svg class="swoosh" viewBox="0 0 231 16" height="16" preserveAspectRatio="none">
    <path d="M0 16 Q110 0 231 4 L231 16 Z" fill="var(--red)"/>
  </svg>
</article>

<article class="piece envelope envelope-b">
  <div class="watermark">KTL</div>
  <div class="wordmark">KTL &amp; Associates</div>
  <div class="sender tiny">2947 Brambleton Way Suite 340<br>Frisco, Texas 75981</div>
  <svg class="swoosh" viewBox="0 0 231 16" height="16" preserveAspectRatio="none">
    <path d="M0 4 Q110 18 231 2 L231 16 L0 16 Z" fill="var(--red)"/>
  </svg>
</article>

<!-- DL envelopes -->
<article class="piece dl dl-back">
  <svg class="flap" viewBox="0 0 250 108" preserveAspectRatio="none">
    <path d="M0 0 L250 0 L125 58 Z" fill="var(--red)"/>
    <path d="M0 108 L125 50 L250 108" fill="none" stroke="#ddd" stroke-width="0.8"/>
  </svg>
  <div class="wordmark">KTL &amp; Associates</div>
</article>

<article class="piece dl dl-front">
  <svg class="flap" viewBox="0 0 250 104" preserveAspectRatio="none">
    <path d="M0 0 L125 36 L250 0 Z" fill="var(--red)"/>
    <path d="M0 104 L125 54 L250 104" fill="none" stroke="#ddd" stroke-width="0.8"/>
  </svg>
  <div class="wordmark">KTL &amp; Associates</div>
</article>

</body>
</html>
```